Menu: A4 (double sided) Lunch/Dinner Menu (one side) + Pizza Menu (other side)

Hello.
We would like to create a new style of menus.
Must be easy to read - a summer feel, crisp, clean, beachy, possible retro feel, colours probably based on our website colours (see address below).
Simple and casual is best as we are a casual beachside Cafe.
This menu will be double sided therefore this job is 2 pages.
If you win this job we will have 2 or 3 more menus for you to create soon after (Drinks, Breakfast, possibly a small Kids menu).
The paper for these menus we expect will be a nice white paper which will then be matte laminated.
Colours possible are the green colour #3a6066, the terracotta on our website logo border and website buttons, maybe a little yellow but must be easy to read on white paper.
Black for text might be okay if this is your best design option.
Please view our website and take a feel for the business, location, the existing website branding and website colours we are trying to achieve, www.tidelinekitchen.com.au
We prefer to avoid overwhelming the guest with too many colours on the menus (hence the white paper) as the building is so colourful (El Prado, Argentina, inspired) and the guest experience can be complimented via crisp easy to read menus.
IMPORTANT:
The menus provided please must be fully and easily editable by us in the future.
If you win the job, you must please provide clear instructions on how our staff can edit the menus in the future if project is delivered in Adobe format. Word is also an option for us if you like.
As such, we have attached some documents: the 2x Word documents for the text, 2x .pdf so you can see the fonts and style we were using previously (was printing on recycled brown paper then matte laminated).
If you wished to use the SeaLife Font (this is the existing Font for headings) please let us know as we purchased that font and can provide it.
We have also attached a menu from Marlowe Tavern which we feel has a nice retro feel.
Please include our Instagram in 1 place on the menu @tidelinekitchen
Finally, please note,
we never wish to waste anyone's time so we will narrow down the submissions quickly based on first drafts (please know this is because we appreciate your effort and know your time is valuable) and we will then work with the top designer to finalise in a professional fashion.
Thank you.

```html
<!DOCTYPE html>
<html lang="en">
<head>
<meta charset="utf-8">
<title>Tideline Kitchen – Lunch + Dinner and Pizza Menus</title>
<link href="https://fonts.googleapis.com/css2?family=Barlow+Condensed:wght@400;500;600&family=Montserrat:wght@800&display=swap" rel="stylesheet">
<style>
  :root{
    --backdrop:#000;
    --paper:#fff;
    --brand-blue:#1f4f91;
    --ink-navy:#1d3a5f;
    --ink-teal:#2c6670;
    --rule:#6f8a96;
    --title-terracotta:#d0672f;
    --title-teal:#2d8c8a;
    --title-gold:#e2a82b;
    --title-rose:#c94a6a;
  }
  *{margin:0;padding:0;box-sizing:border-box}
  html,body{width:1200px;height:800px;overflow:hidden;background:var(--backdrop)}
  body{position:relative;font-family:"Barlow Condensed",sans-serif;color:var(--ink-teal)}

  .menu-page{position:absolute;top:39px;width:502px;height:711px;background:var(--paper);overflow:hidden}
  .menu-page--lunch{left:88px}
  .menu-page--pizza{left:614px}

  .brand-band{position:absolute;left:0;top:0;width:502px;height:60px}
  .brand-name{position:absolute;left:0;top:8px;width:502px;text-align:center;font-family:"Montserrat",sans-serif;font-weight:800;font-size:27px;letter-spacing:1px;color:var(--paper);text-transform:uppercase}

  .page-title{position:absolute;border-radius:3px;background:linear-gradient(90deg,var(--title-terracotta),var(--title-gold) 30%,var(--title-teal) 60%,var(--title-rose))}
  .page-title--lunch{left:120px;top:52px;width:262px;height:30px}
  .page-title--pizza{left:205px;top:50px;width:92px;height:26px}

  .section-heading{position:absolute;display:flex;align-items:center;gap:12px;font-family:"Montserrat",sans-serif;font-weight:800;font-size:19px;line-height:22px;letter-spacing:.5px;color:var(--ink-navy);text-transform:uppercase}
  .section-heading::before,.section-heading::after{content:"";flex:1;height:1px;background:var(--rule)}

  .column{position:absolute;width:190px}
  .column--a{left:43px}
  .column--b{left:270px}

  .item{display:grid;grid-template-columns:1fr auto;margin-bottom:6px}
  .column--entree .item{margin-bottom:4px}
  .column--pizza .item{margin-bottom:7px}
  .item-name{font-weight:600;font-size:14.5px;line-height:15px;color:var(--ink-navy);text-transform:uppercase}
  .item-name small{font-size:11px;font-weight:400;text-transform:none;color:var(--ink-teal)}
  .item-price{font-weight:600;font-size:14.5px;line-height:15px;color:var(--ink-navy);text-align:right;padding-left:6px}
  .item-price small{font-size:10px;font-weight:400}
  .item-desc{grid-column:1 / -1;font-size:11px;line-height:12px;color:var(--ink-teal)}
  .item-desc em{font-style:normal;font-size:9.5px}
  .addon{grid-column:1 / -1;display:flex;justify-content:space-between;font-size:11px;line-height:12px}
  .addon b{font-weight:500;color:var(--ink-navy)}

  .legend{position:absolute;font-size:8px;line-height:10px;color:var(--ink-teal);white-space:nowrap}
  .hours{position:absolute;left:43px;top:644px;font-size:11px;color:var(--ink-navy)}
  .hours b{font-weight:600}
  .contact{position:absolute;left:43px;top:668px;color:var(--ink-navy)}
  .contact-phone{font-size:11px;line-height:18px}
  .contact-phone b{font-size:18px;font-weight:600}
  .contact-address{font-size:11px;line-height:14px;color:var(--ink-teal)}
  .social{position:absolute;right:36px;top:682px;display:flex;align-items:center;gap:5px;font-weight:600;font-size:11.5px;color:var(--ink-navy)}
  .social-mark{width:11px;height:11px;background:var(--ink-navy);border-radius:2px}

  .pizza-intro{position:absolute;left:34px;top:82px;width:440px;font-size:12.5px;color:var(--ink-navy);white-space:nowrap}
  .pizza-allergies{position:absolute;left:34px;top:101px;width:440px;font-size:9px;line-height:12px;color:var(--ink-teal)}
  .pizza-allergies b{color:var(--ink-navy);font-weight:600}
  .sides-bar{position:absolute;left:43px;top:643px;width:416px;border-top:1px solid var(--rule);padding-top:4px;text-align:center;font-weight:600;font-size:13px;color:var(--ink-navy);text-transform:uppercase}
  .sides-bar span{text-transform:none}
</style>
</head>
<body>

<section class="menu-page menu-page--lunch" aria-label="Lunch and dinner menu">
  <svg class="brand-band" viewBox="0 0 502 60" aria-hidden="true"><path d="M0 0H502V46Q251 64 0 46Z" fill="var(--brand-blue)"/></svg>
  <div class="brand-name">Tideline Kitchen</div>
  <div class="page-title page-title--lunch" role="img" aria-label="Decorative multicolour lettering: Lunch + Dinner"></div>

  <h2 class="section-heading" style="left:0;top:88px;width:460px">Entree</h2>
  <div class="column column--a column--entree" style="top:118px">
    <div class="item"><span class="item-name">Garlic Bread (2) <small>v</small></span><span class="item-price">8</span></div>
    <div class="item"><span class="item-name">Salt &amp; Pepper Squid</span><span class="item-price">18</span><span class="item-desc">w/ Thai Dipping Sauce</span></div>
    <div class="item"><span class="item-name">Duo of Dip <small>v</small></span><span class="item-price">14</span><span class="item-desc">w/ Pita</span></div>
    <div class="item"><span class="item-name">Bowl of Chips <small>v</small></span><span class="item-price">11</span><span class="item-desc">w/ Tomato Sauce</span></div>
    <div class="item"><span class="item-name">Seasoned Wedges <small>v</small></span><span class="item-price">15</span><span class="item-desc">w/ Sour Cream &amp; Sweet Chilli</span></div>
  </div>
  <div class="column column--b column--entree" style="top:118px">
    <div class="item"><span class="item-name">Onion Rings (12) <small>v</small></span><span class="item-price">13</span><span class="item-desc">Beer Battered w/ Tangy Mayo</span></div>
    <div class="item"><span class="item-name">Vietnamese Spring Rolls (3)</span><span class="item-price">11</span><span class="item-desc">Chicken, Home-made</span></div>
    <div class="item"><span class="item-name">Bruschetta (1) <small>v</small></span><span class="item-price">10</span><span class="item-desc">w/ Olive Oil, Tomato &amp; Red Onion Salsa, Balsamic Glaze, Feta</span></div>
  </div>

  <h2 class="section-heading" style="left:0;top:258px;width:480px">Mains</h2>
  <div class="column column--a" style="top:285px">
    <div class="item"><span class="item-name">The Fish &amp; Chips</span><span class="item-price">25</span><span class="item-desc">House-crumbed Butterfish<br>w/ Chips, Tartare &amp; Side Salad</span></div>
    <div class="item"><span class="item-name">Smokey Beef<br>&amp; Bacon Cheese Burger</span><span class="item-price" style="align-self:end">23</span><span class="item-desc">w/ Chips, Onion Rings, Gerkins<br>&amp; Tangy Mayo</span><span class="addon">+ Jalapenos<b>+2</b></span><span class="addon">+ Pineapple<b>+2</b></span></div>
    <div class="item"><span class="item-name">Salt &amp; Pepper Squid</span><span class="item-price">31</span><span class="item-desc">Golden Tangles w/ Chips,<br>Thai Dipping Sauce &amp; Side Salad</span></div>
    <div class="item"><span class="item-name">Seafood Basket</span><span class="item-price">31</span><span class="item-desc">Crumbed Butterfish, Grilled Prawns, Salt<br>&amp; Pepper Squid, Chips, Tartare &amp; Side Salad</span></div>
    <div class="item"><span class="item-name">Atlantic Salmon</span><span class="item-price">31</span><span class="item-desc">Served w/ Mash, Teriyaki Sauce<br>&amp; Winter Vegetables <em>(contains breadcrumbs)</em></span></div>
    <div class="item"><span class="item-name">Chicken Parmigiana</span><span class="item-price">27</span><span class="item-desc">House-crumbed Breast Schnitzel,<br>Napoli Sauce, Mozzarella, Chips &amp; Side Salad</span><span class="addon">+ Bacon and Pineapple<b>+4</b></span><span class="addon">+ Jalapenos and Pineapple<b>+4</b></span></div>
  </div>
  <div class="column column--b" style="top:285px;width:196px">
    <div class="item"><span class="item-name">Tideline Platter <small>FOR 2</small></span><span class="item-price">90 <small>(+45 pp)</small></span><span class="item-desc">Beer Battered Flathead, Salt &amp; Pepper Squid, Prawn Skewers, Grilled Chicken, Lamb &amp; Chorizo, Served with Antipasto, Dipping Sauces, Pita &amp; Garlic Bread</span></div>
    <div class="item"><span class="item-name">New York Sirloin <small>gfo</small> 400g</span><span class="item-price">38</span><span class="item-desc">MSA w/ Mash &amp; Winter Vegetables<br>Choose: Mushroom Gravy</span><span class="addon">&nbsp;&nbsp;&nbsp;&nbsp;&nbsp;&nbsp;&nbsp;&nbsp;or Classic Gravy or Surf ‘n’ Turf<b>+6</b></span><span class="item-desc"><em>Please allow 35+ minutes for "well-done"</em></span></div>
    <div class="item"><span class="item-name">Chicken Caesar</span><span class="item-price">27</span><span class="item-desc">w/ Bacon, Anchovies, Egg, Caesar Dressing, Parmesan, Spanish Onion, Garlic Bread</span></div>
    <div class="item"><span class="item-name">Lamb Salad <small>gfo</small></span><span class="item-price">30</span><span class="item-desc">Skewers w/ Traditional Greek Salad,<br>Tzatziki &amp; Garlic Bread</span><span class="addon">+ Extra Lamb<b>+6</b></span></div>
    <div class="item"><span class="item-name">Thai Chicken Curry <small>mild gfo</small></span><span class="item-price">26</span><span class="item-desc">Traditional Recipe, w/ Jasmine Rice<br>&amp; Papadums</span></div>
    <div class="item"><span class="item-name">Beach Burger <small>v</small></span><span class="item-price">23</span><span class="item-desc">House-made Pea &amp; Corn Ricotta Fritter,<br>Pineapple, w/ Wedges, Onion Rings,<br>Sweet Chilli</span></div>
    <div class="item"><span class="item-name">Vegan Curry <small>mild gfo v</small></span><span class="item-price">24</span><span class="item-desc">Chickpea &amp; Pumpkin w/ Fresh Tomatoes<br>&amp; Basil, Jasmine Rice &amp; Papadums</span></div>
  </div>

  <p class="hours">Breakfast to <b>11:15am</b> &nbsp; Lunch from <b>12 noon</b></p>
  <p class="legend" style="left:250px;top:668px">v - Vegetarian • gfo - Gluten Friendly Optional/please ask • mild - Mild Hot</p>
  <div class="contact"><p class="contact-phone">ph <b>8416 2290</b></p><p class="contact-address">18 Shoreline Parade, Seacliff Cove SA 5170</p></div>
  <div class="social"><span class="social-mark"></span>tidelinekitchen</div>
</section>

<section class="menu-page menu-page--pizza" aria-label="Pizza menu">
  <svg class="brand-band" viewBox="0 0 502 60" aria-hidden="true"><path d="M0 0H502V46Q251 64 0 46Z" fill="var(--brand-blue)"/></svg>
  <div class="brand-name">Tideline Kitchen</div>
  <div class="page-title page-title--pizza" role="img" aria-label="Decorative multicolour lettering: Pizza"></div>

  <p class="pizza-intro">ALL 12" With House-made Tomato Base &amp; Mozzarella &nbsp;• &nbsp;Gluten Free Base +$4 &nbsp;• &nbsp;Vegan Cheese +$3</p>
  <p class="pizza-allergies"><b>Allergies?</b> Please let us know! All care is taken to cater for allergies including gluten, however our kitchen is small and we do not have separate preparation or cooking areas. As such, there is risk of cross-contact with your allergen and we are unable to guarantee allergen-free meals. Olives may very rarely contain pips.</p>

  <h2 class="section-heading" style="left:31px;top:146px;width:450px">Standard</h2>
  <div class="column column--a column--pizza" style="top:174px">
    <div class="item"><span class="item-name">Hawaiian</span><span class="item-price">22</span><span class="item-desc">Ham, Pineapple</span></div>
    <div class="item"><span class="item-name">Margherita <small>v</small></span><span class="item-price">22</span><span class="item-desc">Marinated &amp; Diced Tomatoes, Fresh Basil</span></div>
    <div class="item"><span class="item-name">BBQ Chicken</span><span class="item-price">26</span><span class="item-desc">Chicken Salami, Tomato, Spanish Onion,<br>BBQ Sauce</span></div>
    <div class="item"><span class="item-name">Chorizo <small>mh</small></span><span class="item-price">26</span><span class="item-desc">Chorizo, Salami, Tomato, Mushrooms,<br>Spanish Onion</span></div>
    <div class="item"><span class="item-name">Tideline Special</span><span class="item-price">26</span><span class="item-desc">Ham, Salami, Prawns, Kalamata Olives,<br>Roasted Capsicum, Mushrooms,<br>Spanish Onion</span></div>
    <div class="item"><span class="item-name">Meat Lovers</span><span class="item-price">26</span><span class="item-desc">Chicken, Bacon, Salami, Ham, BBQ Sauce</span></div>
  </div>
  <div class="column column--b column--pizza" style="top:174px">
    <div class="item"><span class="item-name">Mona Lisa</span><span class="item-price">26</span><span class="item-desc">Chicken, Pineapple, Ham, Spanish Onion,<br>Mushrooms</span></div>
    <div class="item"><span class="item-name">Puttanesca</span><span class="item-price">26</span><span class="item-desc">Anchovies, Capers, Salami,<br>Kalamata Olives, Roasted Capsicum,<br>Parmesan</span></div>
    <div class="item"><span class="item-name">Tropical Chicken <small>mh</small></span><span class="item-price">26</span><span class="item-desc">Chicken, Pineapple, Spanish Onion,<br>Chilli, Tomato, Mushrooms</span></div>
    <div class="item"><span class="item-name">Vegetarian <small>v</small></span><span class="item-price">26</span><span class="item-desc">Chicken, Roasted Capsicum, Tomato,<br>Mushrooms, Artichokes, Kalamata Olives,<br>Spanish Onion</span></div>
    <div class="item"><span class="item-name">Build Your Own <small>v</small></span><span class="item-price">26</span><span class="item-desc">Tomato Base, Mozzarella &amp; Four Toppings</span></div>
  </div>

  <h2 class="section-heading" style="left:31px;top:430px;width:450px">Gourmet</h2>
  <div class="column column--a column--pizza" style="top:457px">
    <div class="item"><span class="item-name">Caveman</span><span class="item-price">29</span><span class="item-desc">Chicken, Lamb, Pork Sausage, Chorizo,<br>Salami, Bacon, Spanish Onion,<br>Caramelised Onion, Smokey BBQ Sauce</span></div>
    <div class="item"><span class="item-name">Spicy Prawn &amp; Basil Pesto <small>mh</small></span><span class="item-price">29</span><span class="item-desc">Prawns, Roasted Capsicum, Chilli,<br>Spring Onion, Basil Pesto</span></div>
    <div class="item"><span class="item-name">Gourmet Vegetarian <small>v</small></span><span class="item-price">29</span><span class="item-desc">Pumpkin, Eggplant, Semi-dried Tomatoes,<br>Roasted Capsicum, Red Onion,<br>Bulgarian Feta, Kalamata Olives,<br>Spinach</span></div>
  </div>
  <div class="column column--b column--pizza" style="top:457px">
    <div class="item"><span class="item-name">Outlaw <small>h</small></span><span class="item-price">29</span><span class="item-desc">Chilli Jam, Jalapeno Pepper, Mushrooms,<br>Bacon, Chilli, Chorizo, Spanish Onion</span></div>
    <div class="item"><span class="item-name">Lamb Pizza</span><span class="item-price">29</span><span class="item-desc">Lamb, Red Onion, Fresh Tomato,<br>Tzatziki, Spring Onion</span></div>
    <div class="item"><span class="item-name">Los Pollos</span><span class="item-price">29</span><span class="item-desc">Chicken, Pumpkin, Basil Pesto,<br>Spinach, Feta, Pine Nuts</span></div>
    <div class="item"><span class="item-name">Seafood Pizza</span><span class="item-price">29</span><span class="item-desc">Array of Seafood</span></div>
  </div>

  <p class="legend" style="left:344px;top:628px">v - Vegetarian • mh - Mild Hot • h - Hot</p>
  <p class="sides-bar">Garlic Bread <span>$8</span> &nbsp;• &nbsp;Greek Salad <span>$16</span> • &nbsp;Garden Salad &nbsp;<span>$12</span></p>
  <div class="contact"><p class="contact-phone">ph <b>8416 2290</b></p><p class="contact-address">18 Shoreline Parade, Seacliff Cove SA 5170</p></div>
  <div class="social"><span class="social-mark"></span>tidelinekitchen</div>
</section>

</body>
</html>
```